Short term accommodation - Guest feedback flyer

We provide short term fully self contained accommodation for couples,families and friends who require accommodation close to Brisbane City. We have 3 properties - http://www.restnook.com.au/accommodation/qld/brisbane/fernvale. Our properties are advertised on a on a number of online booking sites - such as roam critic, nest finder, restnook etc. Our accommodation is fully self contained, a nest finder from home! Our accommodation is affordable and located near or on transport routes so our guests can travel to all tourist attractions with ease. We provide a personal, professional and family friendly experience and we would like to capture our guests comments on their stay with the view to then posting their comments online so other guests can read about their experiences. Most guests don't have the time to leave their comments online once they check out. Id like a flyer to give to them before they check out so they have time to provide their feedback before they leave, I'll then take their feedback and upload it for them. A lot of travellers like to read online reviews before they book and I'd like the flyer to make it easy for guests to leave their feedback and I'll take it and post it for them. I hope by posting more comments on our webpages that our bookings will increase. Im happy for your to use any of the images/photos that are used on our restnook pages…….ive added the link about. Id like one generic flyer that I can use for all 3 properties please.

Thanks.

```html
<!DOCTYPE html>
<html lang="en">
<head>
<meta charset="utf-8">
<title>Guest Feedback Card</title>
<link rel="stylesheet" href="https://fonts.googleapis.com/css2?family=Tinos:ital,wght@0,400;0,700;1,400;1,700&family=Pinyon+Script&family=Great+Vibes&display=swap">
<style>
  :root {
    --page: #ffffff;
    --damask-light: #8592a9;
    --damask-dark: #5b6c85;
    --ink: #3c3c3c;
    --accent: #e8603c;
    --signature: #f2a068;
    --rule: #555b66;
    --card-white: #ffffff;
  }
  html, body {
    margin: 0;
    padding: 0;
    width: 1200px;
    height: 1000px;
    overflow: hidden;
    background: var(--page);
  }
  .canvas { position: relative; width: 1200px; height: 1000px; }
  .card { position: absolute; left: 314px; width: 572px; height: 448px; }
  .card--front { top: 36px; }
  .card--back { top: 516px; }
  .card svg { display: block; }
  .serif { font-family: "Tinos", "Times New Roman", serif; fill: var(--ink); }
  .script { font-family: "Pinyon Script", cursive; fill: var(--accent); }
  .signature { font-family: "Great Vibes", cursive; fill: var(--signature); }
  .caps-footer { font-family: "Tinos", serif; fill: #ffffff; letter-spacing: 2.4px; font-size: 10px; }
</style>
</head>
<body>
<div class="canvas">

  <!-- Front of card -->
  <div class="card card--front">
    <svg width="572" height="448" viewBox="0 0 572 448">
      <defs>
        <linearGradient id="damaskFill" x1="0" y1="0" x2="1" y2="1">
          <stop offset="0" stop-color="var(--damask-light)"/>
          <stop offset="0.5" stop-color="#7d8ba2"/>
          <stop offset="1" stop-color="var(--damask-dark)"/>
        </linearGradient>
      </defs>
      <rect class="damask" width="572" height="448" fill="url(#damaskFill)" role="img" aria-label="Blue-grey damask floral pattern background"/>
      <g class="seal">
        <circle cx="286" cy="200" r="164" fill="var(--card-white)"/>
        <circle cx="286" cy="200" r="167" fill="none" stroke="var(--card-white)" stroke-width="10" stroke-linecap="round" stroke-dasharray="0 9.3"/>
        <circle cx="286" cy="200" r="160" fill="none" stroke="var(--rule)" stroke-width="1.2" stroke-linecap="round" stroke-dasharray="0.1 3.2"/>
      </g>
      <text class="script" x="286" y="196" text-anchor="middle" font-size="84">Thank You</text>
      <text class="serif" x="286" y="236" text-anchor="middle" font-size="13.5" letter-spacing="0.6">FOR CHOOSING TO STAY WITH US</text>
      <g class="divider" fill="var(--damask-dark)">
        <circle cx="280" cy="257" r="1.6"/><circle cx="286" cy="257" r="2.4"/><circle cx="292" cy="257" r="1.6"/>
      </g>
      <text class="serif" x="286" y="292" text-anchor="middle" font-size="10.5" font-weight="700">WE’D LOVE TO HEAR YOUR FEEDBACK!</text>
      <text class="serif" x="286" y="311" text-anchor="middle" font-size="10" font-style="italic" font-weight="700">Please take a few moments to complete</text>
      <text class="serif" x="286" y="327" text-anchor="middle" font-size="10" font-style="italic" font-weight="700">the reverse of this card.</text>
      <text class="caps-footer" x="286" y="414" text-anchor="middle">LADY MARLOWE HOUSE  |  WILLOWS ON CREST  |  HARTLEY’S</text>
    </svg>
  </div>

  <!-- Back of card -->
  <div class="card card--back">
    <svg width="572" height="448" viewBox="0 0 572 448">
      <defs>
        <linearGradient id="damaskFillBack" x1="0" y1="0" x2="1" y2="1">
          <stop offset="0" stop-color="var(--damask-light)"/>
          <stop offset="0.5" stop-color="#7d8ba2"/>
          <stop offset="1" stop-color="var(--damask-dark)"/>
        </linearGradient>
        <linearGradient id="roomBedroom" x1="0" y1="0" x2="0" y2="1">
          <stop offset="0" stop-color="#c9c2b8"/><stop offset="1" stop-color="#8f857a"/>
        </linearGradient>
        <linearGradient id="roomLounge" x1="0" y1="0" x2="0" y2="1">
          <stop offset="0" stop-color="#b59a7a"/><stop offset="1" stop-color="#3a2c28"/>
        </linearGradient>
        <linearGradient id="roomLiving" x1="0" y1="0" x2="0" y2="1">
          <stop offset="0" stop-color="#d9b470"/><stop offset="1" stop-color="#5a3320"/>
        </linearGradient>
        <clipPath id="cardClip"><rect width="572" height="448"/></clipPath>
      </defs>
      <rect class="damask" width="572" height="448" fill="url(#damaskFillBack)" role="img" aria-label="Blue-grey damask floral pattern background"/>
      <g class="seal" clip-path="url(#cardClip)">
        <circle cx="286" cy="224" r="268" fill="var(--card-white)"/>
        <circle cx="286" cy="224" r="271" fill="none" stroke="var(--card-white)" stroke-width="10" stroke-linecap="round" stroke-dasharray="0 9.3"/>
        <circle cx="286" cy="224" r="263" fill="none" stroke="var(--rule)" stroke-width="1.2" stroke-linecap="round" stroke-dasharray="0.1 3.2"/>
      </g>

      <text class="serif" x="286" y="39" text-anchor="middle" font-size="13" font-weight="700" letter-spacing="0.3">YOUR HOME AWAY FROM HOME!</text>
      <text class="serif" x="286" y="53" text-anchor="middle" font-size="9.5" font-style="italic" font-weight="700">(Please tick which property you stayed at)</text>

      <g class="property">
        <circle cx="163" cy="111" r="48" fill="url(#roomBedroom)" role="img" aria-label="Photo of the Lady Marlowe House bedroom"/>
        <circle cx="163" cy="159" r="7" fill="#fff" stroke="var(--ink)" stroke-width="0.8"/>
        <text class="serif" x="163" y="180" text-anchor="middle" font-size="10" font-weight="700">Lady Marlowe House</text>
      </g>
      <g class="property">
        <circle cx="286" cy="111" r="48" fill="url(#roomLounge)" role="img" aria-label="Photo of the Willows on Crest lounge room"/>
        <circle cx="286" cy="159" r="7" fill="#fff" stroke="var(--ink)" stroke-width="0.8"/>
        <text class="serif" x="286" y="180" text-anchor="middle" font-size="10" font-weight="700">Willows on Crest</text>
      </g>
      <g class="property">
        <circle cx="409" cy="111" r="48" fill="url(#roomLiving)" role="img" aria-label="Photo of the Hartley’s living room"/>
        <circle cx="409" cy="159" r="7" fill="#fff" stroke="var(--ink)" stroke-width="0.8"/>
        <text class="serif" x="409" y="180" text-anchor="middle" font-size="10" font-weight="700">Hartley’s</text>
      </g>

      <text class="serif" x="286" y="214" text-anchor="middle" font-size="10" font-style="italic" font-weight="700">Please tell us in a few words about your experience</text>
      <g class="write-lines" stroke="var(--rule)" stroke-width="1" stroke-linecap="round" stroke-dasharray="0.1 2.6">
        <line x1="86" y1="233" x2="487" y2="233"/>
        <line x1="86" y1="256" x2="487" y2="256"/>
        <line x1="86" y1="279" x2="487" y2="279"/>
      </g>

      <text class="serif" x="286" y="306" text-anchor="middle" font-size="10" font-weight="700">We’d love to post your comments online so that other guests can read them too.</text>
      <text class="serif" x="276" y="322" text-anchor="middle" font-size="10" font-weight="700">Please tick the box to let us know that’s OK</text>
      <circle cx="381" cy="318" r="6.5" fill="#fff" stroke="var(--ink)" stroke-width="0.8"/>

      <text class="serif" x="286" y="346" text-anchor="middle" font-size="10" font-weight="700">Safe travels,</text>
      <text class="signature" x="286" y="371" text-anchor="middle" font-size="22">Maren Holloway</text>

      <g class="listings">
        <circle cx="202" cy="390" r="3.5" fill="var(--ink)"/>
        <text class="serif" x="209" y="393" font-size="9" font-weight="700">roam critic</text>
        <text class="serif" x="257" y="393" font-size="9">|</text>
        <circle cx="272" cy="390" r="3.5" fill="var(--ink)"/>
        <text class="serif" x="279" y="393" font-size="9" font-weight="700">restnook</text>
        <text class="serif" x="318" y="393" font-size="9">|</text>
        <circle cx="333" cy="390" r="3.5" fill="var(--ink)"/>
        <text class="serif" x="340" y="393" font-size="9" font-weight="700">nest finder</text>
      </g>
      <text class="serif" x="286" y="410" text-anchor="middle" font-size="8.5" font-style="italic">You can find us and <tspan font-weight="700">book online</tspan> at roam critic, restnook and nest finder</text>
      <text class="serif" x="286" y="425" text-anchor="middle" font-size="8.5"><tspan font-weight="700">or call</tspan> <tspan font-style="italic">0400 123 456</tspan></text>
    </svg>
  </div>

</div>
</body>
</html>
```